KalVesta Website- Joomla Template

A website for a Plumber company. A one page design ( this is what i mean http://pallowdesign.example/en/#graph)
The website should be a template for Joomla, i will do the website in 3 languages
I want it to be elegant but not so that it looks like a consulting company.
My customers are private customers, my products are :
Main focus is on Fixing 24/7
then renovate bathrooms
replace heating systems
and Maintenance
I need 12 slides:
Who we are
News
Service
Maintenance
Renewable Energy
Sanitary
Heating
Ventilation
Partners
Useful Links
Contact us
of course a Facebook, twitter and G+ icon
try to make an innovative nice menu

```html
<!DOCTYPE html>
<html lang="en">
<head>
<meta charset="utf-8">
<title>KalVesta – Plumbing &amp; Heating</title>
<link href="https://fonts.googleapis.com/css2?family=PT+Sans:wght@400;700&family=PT+Sans+Narrow:wght@400;700&display=swap" rel="stylesheet">
<style>
:root{
  --blue:#0b4c85;
  --blue-dark:#08406f;
  --text:#3a3a3a;
  --muted:#555;
  --line:#d9d9d9;
  --footer:#2c2c2c;
  --footer-bottom:#1f1f1f;
  --white:#fff;
  --date-grey:#8c8c8c;
}
*{box-sizing:border-box;margin:0;padding:0}
html,body{width:1200px;height:2332px;overflow:hidden}
body{position:relative;background:var(--white);font-family:"PT Sans",Arial,sans-serif;color:var(--text)}
.abs{position:absolute}

/* header */
.brand{left:170px;top:14px;width:130px;text-align:center}
.brand-mark{display:block;margin:0 auto 4px;width:30px;height:30px;border-radius:50%;background:var(--blue)}
.brand-name{font-size:22px;color:var(--blue);font-weight:400;letter-spacing:.5px}
.call{left:598px;top:46px;font-size:17px;font-weight:700;color:#222}
.call span{color:var(--blue);font-size:15px;margin-left:6px}
.search{left:801px;top:40px;width:227px;height:38px;border:1px solid #cfcfcf;display:flex}
.search .field{flex:1;font-size:12px;color:#555;padding:12px 16px}
.search .btn{width:40px;background:#d8dde3;display:flex;align-items:center;justify-content:center}

/* nav */
.nav{left:0;top:112px;width:1200px;height:57px;background:var(--blue)}
.nav ul{list-style:none;display:flex;justify-content:space-between;margin:0 171px;height:100%;align-items:center}
.nav li{font-family:"PT Sans Narrow","Arial Narrow",sans-serif;font-weight:700;font-size:13px;color:var(--white)}

/* hero */
.hero{left:0;top:169px;width:1200px;height:492px;background:linear-gradient(90deg,#f4f5f7 0%,#e9ecef 45%,#c8d3df 70%,#8aa6c4 100%)}
.hero-copy{left:75px;top:315px;width:420px}
.hero-copy h1{font-size:35px;color:var(--blue);font-weight:700;letter-spacing:.3px;margin-bottom:20px}
.hero-copy p{font-size:13px;line-height:28px;color:#444}
.btn-read{left:76px;top:482px;width:122px;height:37px;border-radius:19px;background:var(--blue);color:var(--white);font-size:13px;display:flex;align-items:center;justify-content:center}
.dots{left:91px;top:612px;display:flex;gap:6px}
.dots i{width:10px;height:10px;border-radius:50%;background:var(--white)}
.dots i:first-child{background:var(--blue)}

/* services */
.service{top:703px;width:199px;height:267px;border:1px solid #e2e2e2;border-bottom:6px solid var(--blue);text-align:center}
.service .icon{margin:27px auto 0;width:96px;height:104px;display:block}
.service h3{font-size:14.5px;color:var(--blue);font-weight:700;margin-top:8px}
.service p{font-size:10.5px;line-height:18px;color:#555;margin:12px 14px 0}
.more{font-size:11px;color:var(--blue)}
.service .more{display:block;margin-top:8px}
.divider{left:171px;top:1009px;width:858px;height:1px;background:var(--line)}

/* about */
.about-photo{left:173px;top:1056px;width:265px;height:190px;background:linear-gradient(135deg,#8a7b70,#d7d4d0 45%,#9ea3a8)}
.about{left:466px;top:1052px;width:563px}
.about h2{font-size:20px;color:var(--blue);font-weight:700;margin-bottom:10px}
.about p{font-size:10.5px;line-height:21px;color:#444;text-align:justify}
.about .more{display:block;margin-top:14px}

/* who we are */
.who{left:0;top:1290px;width:1200px;height:300px;background:var(--blue)}
.who-copy{left:173px;top:1337px;width:518px;color:var(--white)}
.who-copy h2{font-size:21px;font-weight:700;margin-bottom:14px}
.who-copy p{font-size:10.5px;line-height:21px}
.who-copy .more{color:var(--white);display:block;margin-top:14px}
.video{left:718px;top:1333px;width:321px;height:214px;background:#111}
.video .frame{position:absolute;left:0;top:0;width:321px;height:182px;background:linear-gradient(135deg,#dfe7ef,#6f93bd 55%,#2b5789)}
.video .bar{position:absolute;left:0;top:182px;width:321px;height:32px;background:#1a1a1a}

/* news and testimonials */
.col-title{top:1620px;font-size:21px;font-weight:700;color:var(--blue)}
.news-item{left:171px;width:404px}
.date{position:absolute;left:0;top:0;width:61px;text-align:center}
.date .day{height:37px;border:1px solid #ccc;font-size:19px;font-weight:700;color:#222;line-height:35px}
.date .month{height:37px;background:var(--date-grey);color:var(--white);font-size:13px;line-height:37px}
.news-body{position:absolute;left:85px;top:0;width:320px}
.news-body h4{font-size:13.5px;font-weight:700;color:#222}
.news-body .meta{font-size:11px;color:var(--blue);margin:2px 0 8px}
.news-body p{font-size:10.5px;line-height:19px;color:#555}
.news-body .more{display:block;margin-top:8px}
.news-rule{left:171px;top:1813px;width:404px;height:1px;background:#ccc}
.testi{left:616px;width:406px}
.portrait{position:absolute;left:0;top:0;width:118px;height:98px;border:3px solid #e4e4e4;background:linear-gradient(180deg,#e6e9ee,#b7c0cb)}
.testi .name{position:absolute;left:0;top:105px;width:118px;text-align:center;font-size:11px;color:var(--blue)}
.quote{position:absolute;left:155px;top:0;width:255px;font-size:11px;line-height:20.5px;color:#444;text-align:justify}
.q{position:absolute;font-size:26px;color:#c8c8c8;font-family:Georgia,serif}
.testi-rule{left:616px;top:1813px;width:406px;height:1px;background:#ccc}

/* footer */
.footer{left:0;top:2009px;width:1200px;height:250px;background:var(--footer)}
.footer h5{font-size:18px;font-weight:400;color:var(--white)}
.contact{left:178px;top:2040px;width:220px}
.contact ul{list-style:none;margin-top:20px}
.contact li{display:flex;gap:10px;font-size:11px;color:#e8e8e8;margin-bottom:12px;line-height:14px}
.contact svg{flex:none;margin-top:1px}
.subscribe{left:427px;top:2040px;width:260px}
.subscribe p{font-size:10.5px;line-height:16px;color:#e8e8e8;margin:20px 0 14px}
.sub-field{display:flex;width:249px;height:37px;background:var(--white);border:1px solid #ddd}
.sub-field span{flex:1;font-size:10px;font-style:italic;color:#aaa;padding:12px 14px}
.sub-field b{width:40px;background:var(--blue);display:flex;align-items:center;justify-content:center}
.legal{font-size:10px;color:#e8e8e8;margin-top:14px}
.legal u{margin:0 6px}
.info{left:806px;top:2036px;width:223px}
.input{background:var(--white);font-size:9px;color:#555;padding:0 14px;margin-top:10px;height:29px;line-height:29px;border-radius:2px}
.input.area{height:57px;line-height:22px}
.submit{left:971px;top:2226px;width:58px;height:21px;background:var(--blue);color:var(--white);font-size:10px;font-weight:700;text-align:center;line-height:21px;border-radius:2px}
.bottom{left:0;top:2259px;width:1200px;height:73px;background:var(--footer-bottom)}
.copy{left:173px;top:2288px;font-size:11px;color:#e8e8e8}
.social{left:879px;top:2279px;display:flex;gap:14px}
.social i{width:30px;height:30px;border:2px solid #cfcfcf;border-radius:50%}
</style>
</head>
<body>

<!-- header -->
<div class="abs brand"><span class="brand-mark"></span><span class="brand-name">KalVesta</span></div>
<div class="abs call">Call Us: <span>(123) 045 789 210</span></div>
<div class="abs search">
  <div class="field">Search</div>
  <div class="btn"><svg width="18" height="18" viewBox="0 0 18 18"><circle cx="7" cy="7" r="5.5" fill="none" stroke="#0b4c85" stroke-width="2"/><line x1="11" y1="11" x2="16.5" y2="16.5" stroke="#0b4c85" stroke-width="2.5"/></svg></div>
</div>

<nav class="abs nav"><ul>
  <li>Home</li><li>Who we are</li><li>News</li><li>Service</li><li>Maintenance</li><li>Renewable Energy</li><li>Sanitary</li><li>Heating</li><li>Ventilation</li><li>Air Conditioning</li><li>Partners</li><li>Useful Links</li><li>Contact Us</li>
</ul></nav>

<!-- hero -->
<div class="abs hero" role="img" aria-label="Photo of a smiling plumber in blue overalls holding a wrench in front of pipework"></div>
<div class="abs hero-copy">
  <h1>RENOVATE BATHROOMS</h1>
  <p>consectetuer adipiscing elit. Aenean commodo ligula eget dolor.<br>Aenean massa. Cum sociis natoque penatibus et magnis dis parturi-<br>ent montes, nascetur ridiculus mus.</p>
</div>
<div class="abs btn-read">Read More</div>
<div class="abs dots"><i></i><i></i><i></i><i></i></div>

<!-- services -->
<div class="abs service" style="left:171px">
  <svg class="icon" viewBox="0 0 96 104"><path d="M48 104 L38 92 A48 48 0 1 1 58 92 Z" fill="#0b4c85"/><g transform="rotate(-12 48 48)"><rect x="28" y="36" width="40" height="26" rx="3" fill="#fff"/><circle cx="48" cy="30" r="3" fill="none" stroke="#fff" stroke-width="2"/><text x="48" y="54" text-anchor="middle" font-family="PT Sans,sans-serif" font-weight="700" font-size="13" fill="#0b4c85">24/7</text></g></svg>
  <h3>FIXING 24/7</h3>
  <p>Consectetuer adipiscing elit.Aenean commodo ligula eget dolor. Aenean massa. Cum sociis .</p>
  <span class="more">Read More &raquo;</span>
</div>
<div class="abs service" style="left:391px">
  <svg class="icon" viewBox="0 0 96 104"><path d="M48 104 L38 92 A48 48 0 1 1 58 92 Z" fill="#0b4c85"/><path d="M30 50 V30 a6 6 0 0 1 12 0" fill="none" stroke="#fff" stroke-width="3"/><rect x="24" y="50" width="50" height="5" fill="#fff"/><path d="M27 55 h44 a6 6 0 0 1 -6 12 h-32 a6 6 0 0 1 -6 -12z" fill="#fff"/><line x1="34" y1="67" x2="32" y2="73" stroke="#fff" stroke-width="3"/><line x1="64" y1="67" x2="66" y2="73" stroke="#fff" stroke-width="3"/><circle cx="44" cy="38" r="2" fill="#fff"/><circle cx="48" cy="42" r="2" fill="#fff"/></svg>
  <h3>RENOVATE BATHROOMS</h3>
  <p>Consectetuer adipiscing elit.Aenean commodo ligula eget dolor. Aenean massa. Cum sociis .</p>
  <span class="more">Read More &raquo;</span>
</div>
<div class="abs service" style="left:611px">
  <svg class="icon" viewBox="0 0 96 104"><path d="M48 104 L38 92 A48 48 0 1 1 58 92 Z" fill="#0b4c85"/><g fill="#fff"><rect x="28" y="36" width="5" height="28" rx="2"/><rect x="35" y="36" width="5" height="28" rx="2"/><rect x="42" y="36" width="5" height="28" rx="2"/><rect x="49" y="36" width="5" height="28" rx="2"/><rect x="56" y="36" width="5" height="28" rx="2"/><rect x="63" y="36" width="5" height="28" rx="2"/><rect x="26" y="40" width="44" height="3"/><rect x="26" y="57" width="44" height="3"/><rect x="30" y="64" width="3" height="5"/><rect x="63" y="64" width="3" height="5"/></g></svg>
  <h3>REPLACE HEATING SYSTEMS</h3>
  <p>Consectetuer adipiscing elit.Aenean commodo ligula eget dolor. Aenean massa. Cum sociis .</p>
  <span class="more">Read More &raquo;</span>
</div>
<div class="abs service" style="left:831px">
  <svg class="icon" viewBox="0 0 96 104"><path d="M48 104 L38 92 A48 48 0 1 1 58 92 Z" fill="#0b4c85"/><g fill="#fff"><path d="M30 34 l8 -4 6 8 -4 4 16 16 6 -2 6 8 -6 8 -8 -6 2 -6 -16 -16 -4 4 z"/><path d="M58 32 a8 8 0 1 0 6 6 l-5 2 -3 -3z"/><rect x="32" y="56" width="8" height="14" rx="2" transform="rotate(-45 36 63)"/></g></svg>
  <h3>MAINTENANCE</h3>
  <p>Consectetuer adipiscing elit.Aenean commodo ligula eget dolor. Aenean massa. Cum sociis .</p>
  <span class="more">Read More &raquo;</span>
</div>

<div class="abs divider"></div>

<!-- about -->
<div class="abs about-photo" role="img" aria-label="Close-up photo of a hand tightening a chrome tap with a wrench"></div>
<div class="abs about">
  <h2>ABOUT THE KALVESTA</h2>
  <p>Kanoa Guides are a fun and detailed way to discover the best that Maui has to offer. Whether this is your first trip to Maui or your 101st trip to the island, there is always something different to uncover! From new businesses to new roads, we update our maps often so that you have the most up to date view of what is happening on Maui right now! Wherever you are staying we have the maps to suit your needs! Our "West Maui Map" includes detailed sections of from Lahaina to Kapalua. Our "South Maui Map" covers Maalaea to Wailea and then our "Maui Road Map" gives you a full look at the entire Island including Paia and Makawao.Simply click the</p>
  <span class="more">Read More &raquo;</span>
</div>

<!-- who we are -->
<div class="abs who"></div>
<div class="abs who-copy">
  <h2>WHO WE ARE</h2>
  <p>Kanoa Guides are a fun and detailed way to discover the best that Maui has to offer. Whether this is your first trip to Maui or your 101st trip to the island, there is always something different to uncover! From new businesses to new roads, we update our maps often so that you have the most up to date view of what is happening on Maui right now! Wherever you are staying we have the maps to suit your needs! Our "West Maui Map" includes detailed sections of from Lahaina to Kapalua. Our "South Maui Map" covers Maalaea to Wailea and then our "Maui Road Map" gives you a full look at the entire Island .</p>
  <span class="more">Read More &raquo;</span>
</div>
<div class="abs video">
  <div class="frame" role="img" aria-label="Video still of a plumber with a clipboard giving a thumbs up"></div>
  <div class="bar">
    <svg width="321" height="32" viewBox="0 0 321 32"><rect x="6" y="5" width="26" height="22" fill="#2a2a2a"/><path d="M15 10 L24 16 L15 22Z" fill="#fff"/><rect x="42" y="14" width="225" height="5" fill="#1d5f9a"/><rect x="252" y="2" width="22" height="9" fill="#000"/><text x="263" y="9" text-anchor="middle" font-size="6" fill="#fff" font-family="PT Sans,sans-serif">02:10</text><g fill="#ccc"><rect x="274" y="13" width="2" height="7"/><rect x="278" y="13" width="2" height="7"/><rect x="282" y="13" width="2" height="7"/><rect x="286" y="13" width="2" height="7"/></g><path d="M296 11h4v2h-2v2h-2zM306 11h4v4h-2v-2h-2zM296 19h2v2h2v2h-4zM308 19h2v4h-4v-2h2z" fill="#ccc"/></svg>
  </div>
</div>

<!-- news -->
<div class="abs col-title" style="left:171px">NEWS</div>
<div class="abs col-title" style="left:647px">TESTIMONIALS</div>

<div class="abs news-item" style="top:1680px">
  <div class="date"><div class="day">21</div><div class="month">August</div></div>
  <div class="news-body">
    <h4>Lorem ipsum dolor sit amet</h4>
    <div class="meta">No Comments</div>
    <p>Donec sollicitudin odio urna, et volutpat nulla sagittis eget. Vivamus facilisis libero eu lacus tempor vestibulum. Integer cursus mi magna, vitae pellentesque erat porta vel. Nam eu nibh ut...</p>
    <span class="more">Read More &raquo;</span>
  </div>
</div>
<div class="abs news-rule"></div>
<div class="abs news-item" style="top:1843px">
  <div class="date"><div class="day">20</div><div class="month">August</div></div>
  <div class="news-body">
    <h4>Lorem ipsum dolor sit amet</h4>
    <div class="meta">No Comments</div>
    <p>Donec sollicitudin odio urna, et volutpat nulla sagittis eget. Vivamus facilisis libero eu lacus tempor vestibulum. Integer cursus mi magna, vitae pellentesque erat porta vel. Nam eu nibh ut...</p>
    <span class="more">Read More &raquo;</span>
  </div>
</div>

<!-- testimonials -->
<div class="abs testi" style="top:1683px">
  <div class="portrait" role="img" aria-label="Portrait photo of a male client in a suit"></div>
  <div class="name">Mark Tollen</div>
  <span class="q" style="left:132px;top:-8px">&ldquo;</span>
  <div class="quote">Kanoa Guides are a fun and detailed way to discover the best that Maui has to offer. Whether this is your first trip to Maui or your 101st trip to the island, there is always something different to uncover!</div>
  <span class="q" style="left:213px;top:80px">&rdquo;</span>
</div>
<div class="abs testi-rule"></div>
<div class="abs testi" style="top:1837px">
  <div class="portrait" role="img" aria-label="Portrait photo of a female client"></div>
  <div class="name">Mark Tollen</div>
  <span class="q" style="left:132px;top:-8px">&ldquo;</span>
  <div class="quote">Kanoa Guides are a fun and detailed way to discover the best that Maui has to offer. Whether this is your first trip to Maui or your 101st trip to the island, there is always something different to uncover!</div>
  <span class="q" style="left:213px;top:80px">&rdquo;</span>
</div>

<!-- footer -->
<div class="abs footer"></div>
<div class="abs contact">
  <h5>CONTACT</h5>
  <ul>
    <li><svg width="13" height="12" viewBox="0 0 13 12"><path d="M1 4 Q6.5 0 12 4 L10 5.5 L8.5 4 L4.5 4 L3 5.5Z M3 6 h7 l2 5 h-11z" fill="#ccc"/></svg>000-123-4567 (Phone)</li>
    <li><svg width="13" height="12" viewBox="0 0 13 12"><rect x="3" y="0" width="7" height="4" fill="#ccc"/><rect x="0" y="4" width="13" height="6" rx="1" fill="#ccc"/><rect x="3" y="8" width="7" height="4" fill="#888"/></svg>000-123-4567 (Fax)</li>
    <li><svg width="13" height="12" viewBox="0 0 13 12"><rect x="0" y="2" width="13" height="9" fill="#ccc"/><path d="M0 2 L6.5 7 L13 2" fill="none" stroke="#2c2c2c" stroke-width="1.2"/></svg><u>info@kalvesta.example</u></li>
    <li><svg width="13" height="14" viewBox="0 0 13 14"><path d="M6.5 14 L2 7 A5 5 0 1 1 11 7Z" fill="#ccc"/><circle cx="6.5" cy="5" r="2" fill="#2c2c2c"/></svg><span>KalVesta.,<br>Your Street name,<br>Yout City, Your State.</span></li>
  </ul>
</div>
<div class="abs subscribe">
  <h5>SUBSCRIBE TO OUR NEWSLETTER</h5>
  <p>Enter your email address below to subscribe. You will receive our newsletter once a week.</p>
  <div class="sub-field"><span>enter your email address</span><b><svg width="8" height="10" viewBox="0 0 8 10"><path d="M1 1 L6 5 L1 9" fill="none" stroke="#fff" stroke-width="2"/></svg></b></div>
  <div class="legal"><u style="margin-left:0">Terms of Use</u>|<u>Privacy Policy</u></div>
</div>
<div class="abs info">
  <h5>NEED MORE INFO?</h5>
  <div class="input">NAME</div>
  <div class="input">EMAIL</div>
  <div class="input area">MESSAGE</div>
</div>
<div class="abs submit">SUBMIT</div>

<div class="abs bottom"></div>
<div class="abs copy">Copy right &copy; 2014 &nbsp;KalVesta . All rights reserved.</div>
<div class="abs social"><i></i><i></i><i></i></div>

</body>
</html>
```